labels loose leaf tea business

I am in need of a label redo! I have attatched a couple of our old logo labels (still currently using these labels) also i have our new logo that we have loaded on the website feel free to look. www.brewlark.com i bought the business a year ago and have been wanting to get a new look for a minimal cost.we use the labels that are 4' by 3 1/3' on the bags that hold 100 grams the bag is 5.25"x 8 "stand up pouch and the smaller bag which is 4.25x 6.75" we have used a 2x2 label (which doesn't have room for as much detail. the bags are a matte silver at the time.
i am considering going to either a matte white or there is an aqua co lour not sure if that would work or there is a nice white or silver grey rice paper looking bag i am getting prices.
i would consider a larger label format on this bag as well for retail i need my logo the address and the telephone and website all the ingredients as well as tea type and caffiene content i like to include a short description of the tea, as well as country of origin could be fun.. i have included the steep time and possibly this is something to take into consideration is to make a small info graphic of the steep times that is the same sticker to go on the reverse side of each bag the same.could include the address and website... as you can see my bags have had a different color banner per the type of tea Which my customers are used to that idea pink means fruit black is abrown label blue is herbal etc.
to say what is my style is kind of hard for me i included the two pieces of art work from Northgate Printworks ...the coffee label i liked the bottom part simple and straight forward, (i could also look into seeing how much it would cost to heat stamp my logo on each bag) the second one i do kind of like had drawn also sort of vintage the new logo being aqua and grey to me is fresh and light....really i don't like busy or fussy or Victorian i like a bit unusual ( like the sticker on the kraft paper bag! but it could be a pain to put on straight every time i think the one on the biscotti (art image 3) is kind of neat how its applied the other way...
Anyway my market is some retail/ farmers markets etc.. and website.as well as our own retail shop.we have about 90 kinds of tea so i need to be able to edit and print these myself as to hold stock on labels is not cost effective.
i also should say we use the 4 oz metal tins which i use the same labels size as the large bag but mayb we could design it to fit around the whole tin.
well i hope this is enough info for you and i am super excited to see the products you come up with

Project Deadline Extended Reason: Thank you for taking time to look at my design project. i feel to extend the time as i have never done this before and realize some of you may have better ideas then i have and i feel like you may need more time as well and i have also been talking to some product manufacturers such as the pouches and printer and label makers, i think if possible i will head in the direction of getting a stock label printed where the basic information is pre-printed and i can just change the product detail AS needed.This however may throw a different twist on the labels as i'm not sure that the colored banner such as i had is the way to go.i can see potential in a couple of the designs.However much i wish i could get my logo preprinted ont he bags its not an option at this point its too pricy...so yay keep the designs coming we aren't finished yet! Added Sunday, February 12, 2017

Project Deadline Extended Reason: i am giving five more days, my reason being i have been ill and dont feel like i have the energy to give my full attention too the project as well as we have a wedding on the weekend...i see some close competiton here....and am getting excited as well as nervous as how i will really pick between so many cool designs Added Thursday, February 16, 2017

Project Deadline Extended
Reason: one more deadline... giving some of you designers a chance to get them in that had started on the designs please know this is the last extension and i am not super super excited about any of them yet.....i am looking for a label that can be changed up for the different tea types such as Tamsin provided so far.... so let your imaginations go and become creative, thanks for all the awesome effort so far.....

Target Market(s)

website,farmers markets, retail...seems to cover a broad spectrum of ages

Industry/Entity Type

Business

Colors
86cfc6

Requirements
Must have
• Brewlark is the name
• www.brewlark.com website
• packaged and blended in Canada
• Larkfield Alberta
• 403-718-2045
• 100 grams or 50 grams
• Tea type and name
• the steeping time and water temp and amount of tea
Nice to have
• Discover loose leaf tea at its brightest i s on the logo
• wouldn't have to have it there could take off and put somewhere else
• description of the tea as seen on the old tea labels i would like included

```html
<!DOCTYPE html>
<html lang="en">
<head>
<meta charset="utf-8">
<title>Brewlark – Cucumber Melon Tea Label</title>
<link rel="stylesheet" href="https://fonts.googleapis.com/css2?family=Jost:wght@400;500&family=Arimo:wght@400&display=swap">
<style>
  :root {
    --crimson: #ae2a50;
    --amber: #d9904e;
    --amber-light: #e6ad78;
    --aqua: #86cfc6;
    --teal: #5a9e94;
    --navy: #4a5580;
    --ink: #222;
    --paper: #fff;
  }
  * { margin: 0; padding: 0; box-sizing: border-box; }
  html, body { width: 1200px; height: 780px; overflow: hidden; background: var(--paper); }
  .canvas { position: relative; width: 1200px; height: 780px; }

  /* Front label */
  .front { position: absolute; left: 54px; top: 38px; width: 594px; height: 742px; }
  .pattern-top { position: absolute; left: 0; top: 0; width: 594px; height: 234px; display: block; }
  .brand { position: absolute; left: 0; width: 100%; text-align: center; top: 192px;
    font-family: "Jost", sans-serif; font-weight: 400; font-size: 62px; color: var(--aqua); letter-spacing: 1px; }
  .tagline { position: absolute; left: 0; width: 100%; text-align: center; top: 280px;
    font-family: "Jost", sans-serif; font-size: 14px; letter-spacing: 0.6px; color: var(--aqua); text-transform: uppercase; }
  .tea-band { position: absolute; left: 0; top: 322px; width: 594px; height: 105px; background: var(--crimson);
    color: var(--paper); text-align: center; font-family: "Jost", sans-serif; }
  .tea-name { font-size: 56px; font-weight: 400; font-variant: small-caps; letter-spacing: 2.5px; line-height: 1; padding-top: 10px; }
  .tea-type { font-size: 17px; letter-spacing: 0.4px; margin-top: 8px; text-transform: uppercase; }
  .description { position: absolute; left: 20px; right: 20px; top: 465px; text-align: center;
    font-family: "Arimo", sans-serif; font-size: 22px; line-height: 27px; color: var(--ink); }
  .divider-dots { position: absolute; left: 0; width: 100%; top: 533px; height: 12px; display: block; }
  .facts { position: absolute; left: 0; top: 557px; width: 594px; height: 50px;
    border-top: 1.5px solid var(--crimson); border-bottom: 1.5px solid var(--crimson);
    display: flex; justify-content: center; align-items: center; gap: 34px;
    font-family: "Jost", sans-serif; color: var(--teal); }
  .weight { font-size: 20px; letter-spacing: 1px; }
  .servings { font-size: 16px; font-variant: small-caps; letter-spacing: 0.6px; }
  .cup-icon { width: 36px; height: 32px; }
  .pattern-bottom { position: absolute; left: 0; top: 627px; width: 594px; height: 115px; display: block; }
  .ingredients { position: absolute; left: 60px; right: 60px; top: 615px; text-align: center;
    font-family: "Jost", sans-serif; font-size: 13px; font-weight: 500; line-height: 17px; font-variant: small-caps;
    letter-spacing: 0.5px; color: var(--ink); }

  /* Back sticker */
  .back { position: absolute; left: 717px; top: 170px; width: 445px; height: 285px; }
  .origin { text-align: center; font-family: "Arimo", sans-serif; font-size: 13.5px; color: var(--ink); padding-top: 3px; height: 31px; }
  .brew-guide { display: flex; height: 104px; border-top: 1.5px solid var(--amber); border-bottom: 1.5px solid var(--amber); }
  .brew-step { flex: 1; display: flex; flex-direction: column; align-items: center; padding-top: 20px;
    font-family: "Jost", sans-serif; font-size: 13px; font-weight: 500; font-variant: small-caps; letter-spacing: 0.8px; color: var(--ink); }
  .brew-step + .brew-step { border-left: 1.5px solid var(--amber); }
  .brew-step svg { margin-top: 12px; }
  .contact-bar { margin-top: 15px; height: 29px; background: var(--amber); color: var(--paper);
    font-family: "Arimo", sans-serif; font-size: 15px; display: flex; align-items: center; padding-left: 11px; gap: 10px; }
  .contact-bar .sep { font-size: 10px; }
  .pattern-strip { display: block; margin-top: 20px; width: 445px; height: 86px; }
</style>
</head>
<body>
<main class="canvas">

  <section class="front">
    <svg class="pattern-top" viewBox="0 0 594 234" role="img" aria-label="Decorative amber lattice pattern with crimson star tiles">
      <defs>
        <linearGradient id="lattice-top" x1="0" y1="0" x2="1" y2="1">
          <stop offset="0" stop-color="#e6ad78"/>
          <stop offset="1" stop-color="#d9904e"/>
        </linearGradient>
      </defs>
      <rect width="594" height="234" fill="url(#lattice-top)"/>
      <path d="M0 234 Q297 6 594 234 Z" fill="#fff"/>
    </svg>

    <div class="brand">Brewlark</div>
    <div class="tagline">Discover loose leaf tea at its brightest</div>

    <div class="tea-band">
      <h1 class="tea-name">Cucumber Melon</h1>
      <p class="tea-type">Caffeine free loose / fruit tea</p>
    </div>

    <p class="description">Sweet sugary notes of butterscotch blend in perfect harmony with the decadent characteristics of pu-erh.</p>

    <svg class="divider-dots" viewBox="0 0 594 12">
      <g fill="var(--navy)">
        <rect x="186" y="2" width="6" height="6" transform="rotate(45 189 5)"/>
        <rect x="203" y="2" width="6" height="6" transform="rotate(45 206 5)"/>
        <rect x="220" y="2" width="6" height="6" transform="rotate(45 223 5)"/>
        <rect x="237" y="2" width="6" height="6" transform="rotate(45 240 5)"/>
        <rect x="254" y="2" width="6" height="6" transform="rotate(45 257 5)"/>
        <rect x="271" y="2" width="6" height="6" transform="rotate(45 274 5)"/>
        <rect x="315" y="2" width="6" height="6" transform="rotate(45 318 5)"/>
        <rect x="332" y="2" width="6" height="6" transform="rotate(45 335 5)"/>
        <rect x="349" y="2" width="6" height="6" transform="rotate(45 352 5)"/>
        <rect x="366" y="2" width="6" height="6" transform="rotate(45 369 5)"/>
        <rect x="383" y="2" width="6" height="6" transform="rotate(45 386 5)"/>
        <rect x="400" y="2" width="6" height="6" transform="rotate(45 403 5)"/>
      </g>
    </svg>

    <div class="facts">
      <span class="weight">100GR</span>
      <svg class="cup-icon" viewBox="0 0 36 32" fill="none" stroke="var(--teal)" stroke-width="1.6" stroke-linecap="round">
        <path d="M13 2 q-2 3 0 5 q2 3 0 6"/>
        <path d="M18 2 q-2 3 0 5 q2 3 0 6"/>
        <path d="M23 2 q-2 3 0 5 q2 3 0 6"/>
        <path d="M5 16 h22 v4 a8 6 0 0 1 -8 6 h-6 a8 6 0 0 1 -8 -6 z"/>
        <path d="M27 18 h3 a3 3 0 0 1 0 6 h-4"/>
        <path d="M3 29 h28"/>
      </svg>
      <span class="servings">38-50 servings</span>
    </div>

    <svg class="pattern-bottom" viewBox="0 0 594 115" role="img" aria-label="Decorative amber lattice pattern with crimson star tiles">
      <defs>
        <linearGradient id="lattice-bottom" x1="0" y1="0" x2="1" y2="1">
          <stop offset="0" stop-color="#e6ad78"/>
          <stop offset="1" stop-color="#d9904e"/>
        </linearGradient>
      </defs>
      <rect width="594" height="115" fill="url(#lattice-bottom)"/>
      <path d="M0 0 L594 0 Q297 180 0 0 Z" fill="#fff"/>
    </svg>

    <p class="ingredients">Ingredients: luxury natural dried apple pieces,<br>hibiscus, rosehip natural dried orange,<br>calendula petals, natural flavors.</p>
  </section>

  <section class="back">
    <p class="origin">PACKAGED AND BLENDED IN CANADA</p>
    <div class="brew-guide">
      <div class="brew-step">
        <span>boiling (212°)</span>
        <svg width="122" height="36" viewBox="0 0 122 36" fill="none" stroke="var(--crimson)" stroke-width="2">
          <circle cx="18" cy="18" r="15"/>
          <circle cx="18" cy="18" r="8" fill="var(--crimson)"/>
          <path d="M32 11 h84 a6 6 0 0 1 0 14 h-84"/>
          <rect x="26" y="15" width="45" height="6" fill="var(--crimson)" stroke="none"/>
          <path d="M92 11 v5 M98 11 v5 M104 11 v5 M110 11 v5" stroke-width="1.5"/>
        </svg>
      </div>
      <div class="brew-step">
        <span>5 minutes</span>
        <svg width="50" height="50" viewBox="0 0 50 50" fill="none" stroke="var(--crimson)" stroke-width="2.5">
          <circle cx="25" cy="25" r="22"/>
          <circle cx="25" cy="25" r="16" stroke-width="1.5"/>
          <path d="M25 15 v10 l8 -4" stroke-linecap="round"/>
          <path d="M25 5 v3 M25 42 v3 M5 25 h3 M42 25 h3" stroke-width="2"/>
        </svg>
      </div>
      <div class="brew-step">
        <span>1 ½ tsp per 8 oz</span>
        <svg width="100" height="36" viewBox="0 0 100 36" fill="none" stroke="var(--crimson)" stroke-width="2">
          <path d="M4 14 h44"/>
          <path d="M4 14 a3 3 0 0 0 0 6 h40"/>
          <path d="M48 12 h44 a22 20 0 0 1 -44 0 z" fill="#fff"/>
          <path d="M50 12 h40" stroke-width="4"/>
        </svg>
      </div>
    </div>
    <div class="contact-bar">
      <span>Larkfield Alberta</span><span class="sep">◆</span>
      <span>403-718-2045</span><span class="sep">◆</span>
      <span>www.brewlark.com</span>
    </div>
    <svg class="pattern-strip" viewBox="0 0 445 86" role="img" aria-label="Decorative amber lattice strip with crimson star tiles">
      <defs>
        <linearGradient id="lattice-strip" x1="0" y1="0" x2="1" y2="0">
          <stop offset="0" stop-color="#e6ad78"/>
          <stop offset="1" stop-color="#d9904e"/>
        </linearGradient>
      </defs>
      <rect width="445" height="86" fill="url(#lattice-strip)"/>
    </svg>
  </section>

</main>
</body>
</html>
```